Get me out of Jail business cards!!!!

I need business cards done for my business. I own a BailBonds and I get people out of jail!

Colors are red white and black

I need it to say on the card these details:

Freedom Hop Bailbonds

427 S Calloway St
Arcadia, FL 34266

863-555-0187

Open 24/7

On the back of the card:

Must check in every Tuesday.

______/______/______ court date
____________________ time
You must know your court date at all times!

Marla Whitcombe - owner
Jolene Whitcombe - agent
Rosalind Pickett - agent

Industry/Entity Type

Bail bonds

Contact Information for Business Card

Colors are red white and black I need it to say on the card these details: Freedom Hop Bailbonds 427 S Calloway St Arcadia, FL 34266 863-555-0187 Open 24/7 On the back of the card: Must check in every Tuesday. ______/______/______ court date ____________________ time You must know your court date at all times! Marla Whitcombe - owner Jolene Whitcombe - agent Rosalind Pickett - agent

Font styles to use
Serif
Sans Serif

Colors
EB3D1F
EC4F4E
F09395
F8D3D4
FCEDEE

Requirements
Must have
• I listed the must haves in the business card details
Nice to have
• Handcuffs or jail bars or a man in a black and white suit

```html
<!DOCTYPE html>
<html lang="en">
<head>
<meta charset="utf-8">
<title>Freedom Hop Bailbonds – Business Card</title>
<link rel="stylesheet" href="https://fonts.googleapis.com/css2?family=Poppins:wght@400;500&display=swap">
<style>
  :root {
    --page: #7a7a7a;
    --ink: #000000;
    --paper: #ffffff;
    --text-dark: #1a1a1a;
    --text-muted: #4a4a4a;
    --red: #ec1c1c;
    --corridor-dark-a: #2a2a2a;
    --corridor-dark-b: #0b0b0b;
    --corridor-light-a: #e4ebee;
    --corridor-light-b: #cfd9dd;
  }
  * { margin: 0; padding: 0; box-sizing: border-box; }
  html, body {
    width: 1093px; height: 1200px; overflow: hidden;
    background: var(--page);
    font-family: "Poppins", sans-serif;
  }
  .card {
    position: absolute;
    left: 265px;
    width: 580px;
    height: 360px;
    border-radius: 30px;
    overflow: hidden;
    box-shadow: 0 4px 10px rgba(0,0,0,0.35);
  }
  /* Front */
  .card--front { top: 226px; background: var(--ink); color: var(--paper); }
  .card--front .corridor-photo {
    position: absolute; inset: 0;
    background: radial-gradient(ellipse at 55% 40%, #4a4a4a 0%, var(--corridor-dark-a) 35%, var(--corridor-dark-b) 85%);
  }
  .card--front .top-band {
    position: absolute; left: 0; right: 0; top: 0; height: 70px;
    background: linear-gradient(#000 0%, rgba(0,0,0,0.85) 100%);
  }
  .phone, .hours {
    position: absolute; top: 24px;
    font-size: 22px; font-weight: 500; letter-spacing: 0.5px;
  }
  .phone { left: 37px; }
  .hours { right: 36px; }
  .brand {
    position: absolute; left: 0; right: 0; top: 188px;
    text-align: center; font-weight: 400; color: var(--paper); line-height: 1;
  }
  .brand__line1 { display: block; font-size: 36px; }
  .brand__line2 { display: block; font-size: 64px; margin-top: 4px; letter-spacing: 1px; }
  .address {
    position: absolute; left: 0; right: 0; top: 308px;
    text-align: center; font-size: 17px;
  }
  /* Back */
  .card--back { top: 621px; background: var(--ink); }
  .card--back .corridor-photo {
    position: absolute; left: 0; right: 0; top: 0; height: 236px;
    background: linear-gradient(180deg, #f2f5f6 0%, var(--corridor-light-a) 45%, var(--corridor-light-b) 100%);
  }
  .checkin {
    position: absolute; left: 0; right: 0; top: 38px;
    text-align: center; font-size: 21px; font-weight: 500; color: var(--text-dark);
  }
  .field {
    position: absolute; font-size: 17px; color: var(--text-muted); white-space: nowrap;
  }
  .field--date { left: 105px; top: 91px; }
  .field--time { left: 151px; top: 133px; }
  .field__blank { letter-spacing: 1px; }
  .warning {
    position: absolute; left: 0; right: 0; top: 178px;
    text-align: center; font-size: 17px; font-weight: 500; color: var(--red);
  }
  .staff {
    position: absolute; left: 0; right: 0; top: 281px;
    display: flex; justify-content: space-around; padding: 0 22px;
    list-style: none; text-align: center; line-height: 1.25;
  }
  .staff__name { display: block; font-size: 17px; font-weight: 500; color: var(--paper); }
  .staff__role { display: block; font-size: 17px; color: var(--red); }
</style>
</head>
<body>
  <section class="card card--front">
    <div class="corridor-photo" role="img" aria-label="Dark black and white photograph of a jail corridor lined with cell bars"></div>
    <div class="top-band"></div>
    <p class="phone">863-555-0187</p>
    <p class="hours">Open 24/7</p>
    <h1 class="brand">
      <span class="brand__line1">Freedom Hop</span>
      <span class="brand__line2">Bailbonds</span>
    </h1>
    <p class="address">427 S Calloway St, Arcadia, FL 34266</p>
  </section>

  <section class="card card--back">
    <div class="corridor-photo" role="img" aria-label="Faded light photograph of a jail corridor with cell bars"></div>
    <p class="checkin">Must check in every Tuesday.</p>
    <p class="field field--date">Court date: <span class="field__blank">______/______/______</span></p>
    <p class="field field--time">Time: <span class="field__blank">______________________</span></p>
    <p class="warning">You must know your court date at all times!</p>
    <ul class="staff">
      <li><span class="staff__name">Marla Whitcombe</span><span class="staff__role">Owner</span></li>
      <li><span class="staff__name">Jolene Whitcombe</span><span class="staff__role">Agent</span></li>
      <li><span class="staff__name">Rosalind Pickett</span><span class="staff__role">Agent</span></li>
    </ul>
  </section>
</body>
</html>
```